Trading journal (Corvanta Loop)

I need a design for trading journal application.
I would like to start from dark version of the design and the main goal that it should be pretty intuitive for everyone. I am going to create the app from scratch and I don't have any logo or branding colors, so it is up to you to choose a color scheme but it is a dark mode, so one of the colors would be black obviously.
The app will be available for web PC, Android and iOS.

There is google document with the requirements.
https://files.plomivex.net/sheet/7QwZrT2kLpN9vB4xHs0Jd8YcGm3FaUe6/view?mode=open

Target Market(s)

Professional traders

Industry/Entity Type

Trading

Colors

Designer to choose colors to be used in the design.

Requirements
Must have
• Dark mode design for PC and mobile views, the design must be pretty intuitive for everyone.
Nice to have
• Tooltips for something non obvious; popovers after completing some actions

```html
<!DOCTYPE html>
<html lang="en">
<head>
<meta charset="utf-8">
<title>Corvanta Loop – Trading Journal</title>
<link href="https://fonts.googleapis.com/css2?family=Oswald:wght@500;600;700&family=Mulish:ital,wght@0,300;0,400;0,600;0,700;0,800;1,300;1,400&display=swap" rel="stylesheet">
<style>
  :root{
    --page:#ffffff;
    --app:#000000;
    --sidebar:#0e0e0e;
    --card:#141414;
    --teal:#03b5b5;
    --teal-dark:#0a6577;
    --text:#ffffff;
    --muted:#e6e6e6;
    --line:#4a4a4a;
    --grid:#3a3a3a;
    --lime:#a6cf3a;
    --magenta:#e5197a;
  }
  *{box-sizing:border-box;margin:0;padding:0}
  html,body{width:1200px;height:2284px;overflow:hidden;background:var(--page)}
  body{position:relative;font-family:"Mulish",sans-serif;color:var(--text)}
  .screen{position:absolute;left:80px;width:1166px;height:734px;background:var(--app);transform:scale(0.8785);transform-origin:0 0;overflow:hidden}
  .screen--welcome{top:77px}
  .screen--profile{top:795px}
  .screen--dashboard{top:1504px}
  .abs{position:absolute}
  .sidebar{left:0;top:0;width:169px;height:734px;background:var(--sidebar)}
  .brand{left:38px;top:22px;font-family:"Oswald",sans-serif;font-weight:700;font-size:27px;line-height:28px;letter-spacing:.3px}
  .nav-item{left:0;width:165px;height:40px;padding-left:35px;line-height:40px;font-size:14px;font-weight:300}
  .nav-item--active{background:var(--teal-dark)}
  .sync{left:840px;font-size:12px;font-weight:400;color:var(--muted)}
  .avatar{left:1036px;top:30px;width:34px;height:34px;border-radius:50%;background:radial-gradient(circle at 50% 40%,#d9c2a8,#8a7560)}
  .user{left:1086px;top:24px;font-size:13px;font-weight:400}
  .logout{left:1086px;top:48px;width:61px;height:18px;background:var(--teal);font-size:10px;line-height:18px;text-align:center;letter-spacing:.4px}
  .copyright{left:0;width:1304px;top:683px;text-align:center;font-size:13px;font-weight:300}
  .welcome{left:287px;top:182px;width:756px;height:366px;background:var(--teal);text-align:center}
  .welcome h1{margin-top:60px;font-family:"Oswald",sans-serif;font-weight:600;font-size:40px;line-height:48px;letter-spacing:.5px}
  .welcome .rule{width:64px;height:3px;background:var(--text);margin:22px auto 32px}
  .welcome p{font-style:italic;font-weight:300;font-size:27px;line-height:43px;padding:0 90px}
  .heading{font-family:"Oswald",sans-serif;font-weight:600;font-size:30px;line-height:36px}
  .field{width:386px;height:56px;border:1px solid var(--line);padding-left:27px;font-size:13px;line-height:54px;font-weight:300}
  .field svg{position:absolute;right:24px;top:21px}
  .submit{left:259px;top:419px;width:128px;height:56px;background:var(--teal);font-weight:800;font-size:20px;line-height:56px;text-align:center;letter-spacing:.5px}
  .stat{top:101px;width:180px;height:102px;background:var(--card);padding:28px 0 0 26px}
  .stat-value{color:var(--teal);font-weight:700;font-size:17px;line-height:22px}
  .stat-label{margin-top:6px;font-size:13px;line-height:15px;font-weight:400;text-transform:uppercase}
  .section-title{font-family:"Oswald",sans-serif;font-weight:500;font-size:22px;line-height:28px}
  .tab{font-size:13px;height:48px;line-height:48px;text-align:center}
  .tab--active{background:var(--teal-dark)}
  .trades{left:810px;top:286px;width:338px;height:343px;background:var(--card)}
  .trade{left:0;width:338px;height:80px}
  .trade-mark{left:20px;top:8px;width:38px;height:38px}
  .trade-name{left:75px;top:-6px;font-size:12px;font-weight:700}
  .trade-col{top:16px}
  .trade-col small{display:block;font-size:8px;font-weight:400;letter-spacing:.1px}
  .trade-col span{display:block;font-size:12px;margin-top:3px}
  .badge{display:inline-block;background:var(--teal);font-size:10px;padding:0 5px;margin-left:3px;color:#e8ffff;font-style:normal}
  .sep{left:6px;width:322px;height:1px;background:#2a2a2a}
</style>
</head>
<body>

<section class="screen screen--welcome">
  <aside class="abs sidebar">
    <div class="abs brand">TRADING<br>JOURNAL</div>
    <div class="abs nav-item" style="top:101px">Home</div>
    <div class="abs nav-item" style="top:148px">Trade</div>
    <div class="abs nav-item" style="top:195px">Import trades</div>
    <div class="abs nav-item" style="top:241px">Calendar</div>
    <div class="abs nav-item" style="top:288px">Subscriptions</div>
    <div class="abs nav-item" style="top:335px">Settings</div>
  </aside>
  <div class="abs sync" style="top:26px">Last data synced</div>
  <div class="abs sync" style="top:50px">16 January &nbsp;|&nbsp;&nbsp; 10:00pm</div>
  <div class="abs avatar" role="img" aria-label="User profile photo"></div>
  <div class="abs user">MARLOW</div>
  <div class="abs logout">LOGOUT</div>
  <div class="abs welcome">
    <h1>WELCOME TO CORVANTA LOOP</h1>
    <div class="rule"></div>
    <p>Corvanta Loop helps you learn from your trade mistakes and become a profitable trader with the power of journaling and analytics.</p>
  </div>
  <div class="abs copyright">Copyright © 2024 All Rights Reserved</div>
</section>

<section class="screen screen--profile">
  <aside class="abs sidebar">
    <div class="abs brand">TRADING<br>JOURNAL</div>
    <div class="abs nav-item" style="top:101px">Home</div>
    <div class="abs nav-item" style="top:148px">Trade</div>
    <div class="abs nav-item" style="top:195px">Import trades</div>
    <div class="abs nav-item" style="top:241px">Calendar</div>
    <div class="abs nav-item" style="top:288px">Subscriptions</div>
    <div class="abs nav-item" style="top:335px">Settings</div>
  </aside>
  <div class="abs sync" style="top:26px">Last data synced</div>
  <div class="abs sync" style="top:50px">16 January &nbsp;|&nbsp;&nbsp; 10:00pm</div>
  <div class="abs avatar" role="img" aria-label="User profile photo"></div>
  <div class="abs user">MARLOW</div>
  <div class="abs logout">LOGOUT</div>
  <h2 class="abs heading" style="left:259px;top:178px">SELECT PROFILE</h2>
  <div class="abs field" style="left:259px;top:247px">Enter Display Name</div>
  <div class="abs field" style="left:673px;top:247px">What is your default account currency?
    <svg width="14" height="9" viewBox="0 0 14 9"><path d="M1 1l6 6 6-6" fill="none" stroke="#fff" stroke-width="1.4"/></svg></div>
  <div class="abs field" style="left:259px;top:329px">What is your default time zone?
    <svg width="14" height="9" viewBox="0 0 14 9"><path d="M1 1l6 6 6-6" fill="none" stroke="#fff" stroke-width="1.4"/></svg></div>
  <div class="abs field" style="left:673px;top:329px">What is your trading experience?
    <svg width="14" height="9" viewBox="0 0 14 9"><path d="M1 1l6 6 6-6" fill="none" stroke="#fff" stroke-width="1.4"/></svg></div>
  <div class="abs submit">SUBMIT</div>
  <div class="abs copyright">Copyright © 2024 All Rights Reserved</div>
</section>

<section class="screen screen--dashboard">
  <aside class="abs sidebar">
    <div class="abs brand">TRADING<br>JOURNAL</div>
    <div class="abs nav-item nav-item--active" style="top:101px">Home</div>
    <div class="abs nav-item" style="top:148px">Trade</div>
    <div class="abs nav-item" style="top:195px">Import trades</div>
    <div class="abs nav-item" style="top:241px">Calendar</div>
    <div class="abs nav-item" style="top:288px">Subscriptions</div>
    <div class="abs nav-item" style="top:335px">Settings</div>
  </aside>
  <div class="abs sync" style="top:26px">Last data synced</div>
  <div class="abs sync" style="top:50px">16 January &nbsp;|&nbsp;&nbsp; 10:00pm</div>
  <div class="abs avatar" role="img" aria-label="User profile photo"></div>
  <div class="abs user">MARLOW</div>
  <div class="abs logout">LOGOUT</div>

  <div class="abs stat" style="left:192px"><div class="stat-value">$1456647552</div><div class="stat-label">Total net profit</div></div>
  <div class="abs stat" style="left:389px"><div class="stat-value">32546</div><div class="stat-label">Average win/loss</div></div>
  <div class="abs stat" style="left:584px"><div class="stat-value">87945</div><div class="stat-label">Total number of<br>trades</div></div>
  <div class="abs stat" style="left:778px"><div class="stat-value">85%</div><div class="stat-label">Win rate</div></div>
  <div class="abs stat" style="left:970px"><div class="stat-value">$35624</div><div class="stat-label">Fees + commissions</div></div>

  <h3 class="abs section-title" style="left:195px;top:234px">P&amp;L GRAPH WITH GROSS</h3>
  <svg class="abs" style="left:185px;top:285px" width="610" height="360" viewBox="185 285 610 360" font-family="Mulish, sans-serif">
    <g stroke="var(--grid)" stroke-width="1">
      <line x1="205" y1="293" x2="778" y2="293"/><line x1="205" y1="324.7" x2="778" y2="324.7"/>
      <line x1="205" y1="356.4" x2="778" y2="356.4"/><line x1="205" y1="388.1" x2="778" y2="388.1"/>
      <line x1="205" y1="419.8" x2="778" y2="419.8"/><line x1="205" y1="451.5" x2="778" y2="451.5"/>
      <line x1="205" y1="483.2" x2="778" y2="483.2"/><line x1="205" y1="514.9" x2="778" y2="514.9"/>
      <line x1="205" y1="546.6" x2="778" y2="546.6"/><line x1="205" y1="578.3" x2="778" y2="578.3"/>
      <line x1="205" y1="610" x2="778" y2="610"/>
      <line x1="205" y1="293" x2="205" y2="610"/><line x1="252" y1="293" x2="252" y2="610"/>
      <line x1="300" y1="293" x2="300" y2="610"/><line x1="348" y1="293" x2="348" y2="610"/>
      <line x1="396" y1="293" x2="396" y2="610"/><line x1="444" y1="293" x2="444" y2="610"/>
      <line x1="491" y1="293" x2="491" y2="610"/><line x1="539" y1="293" x2="539" y2="610"/>
      <line x1="587" y1="293" x2="587" y2="610"/><line x1="635" y1="293" x2="635" y2="610"/>
      <line x1="683" y1="293" x2="683" y2="610"/><line x1="731" y1="293" x2="731" y2="610"/>
      <line x1="778" y1="293" x2="778" y2="610"/>
    </g>
    <g fill="#8a8a8a" font-size="6" text-anchor="end">
      <text x="200" y="295">100</text><text x="200" y="327">90</text><text x="200" y="358">80</text>
      <text x="200" y="390">70</text><text x="200" y="422">60</text><text x="200" y="453">50</text>
      <text x="200" y="485">40</text><text x="200" y="517">30</text><text x="200" y="548">20</text>
      <text x="200" y="580">10</text><text x="200" y="612">0</text>
    </g>
    <g fill="#8a8a8a" font-size="6" text-anchor="middle">
      <text x="227" y="632">JAN</text><text x="275" y="632">FEB</text><text x="323" y="632">MAR</text>
      <text x="371" y="632">APR</text><text x="419" y="632">MAY</text><text x="468" y="632">JUN</text>
      <text x="516" y="632">JUL</text><text x="564" y="632">AUG</text><text x="611" y="632">SEP</text>
      <text x="659" y="632">OCT</text><text x="706" y="632">NOV</text><text x="755" y="632">DEC</text>
    </g>
    <polyline fill="none" stroke="var(--lime)" stroke-width="1.5"
      points="205,483.2 252,451.5 300,483.2 348,388.1 396,388.1 444,419.8 491,388.1 539,388.1 587,337 635,324.7 683,324.7 731,337 778,324.7"/>
    <g fill="var(--lime)">
      <circle cx="205" cy="483.2" r="3"/><circle cx="252" cy="451.5" r="3"/><circle cx="300" cy="483.2" r="3"/>
      <circle cx="348" cy="388.1" r="3"/><circle cx="396" cy="388.1" r="3"/><circle cx="444" cy="419.8" r="3"/>
      <circle cx="491" cy="388.1" r="3"/><circle cx="539" cy="388.1" r="3"/><circle cx="587" cy="337" r="3"/>
      <circle cx="635" cy="324.7" r="3"/><circle cx="683" cy="324.7" r="3"/><circle cx="731" cy="337" r="3"/>
      <circle cx="778" cy="324.7" r="3"/>
    </g>
    <polyline fill="none" stroke="var(--magenta)" stroke-width="1.5"
      points="205,578.3 252,514.9 300,546.6 348,451.5 396,419.8 444,483.2 491,451.5 539,483.2 635,356.4 731,419.8 778,356.4"/>
    <g fill="var(--magenta)">
      <circle cx="205" cy="578.3" r="3"/><circle cx="252" cy="514.9" r="3"/><circle cx="300" cy="546.6" r="3"/>
      <circle cx="348" cy="451.5" r="3"/><circle cx="396" cy="419.8" r="3"/><circle cx="444" cy="483.2" r="3"/>
      <circle cx="491" cy="451.5" r="3"/><circle cx="539" cy="483.2" r="3"/><circle cx="635" cy="356.4" r="3"/>
      <circle cx="731" cy="419.8" r="3"/><circle cx="778" cy="356.4" r="3"/>
    </g>
  </svg>

  <h3 class="abs section-title" style="left:811px;top:239px">TRADES</h3>
  <div class="abs tab tab--active" style="left:1003px;top:237px;width:74px">OPENED</div>
  <div class="abs tab" style="left:1090px;top:237px;width:70px">RECENT</div>

  <div class="abs trades">
    <div class="abs trade" style="top:25px">
      <div class="abs trade-mark" style="background:#e8e8e8" role="img" aria-label="Halvern ticker symbol"></div>
      <div class="abs trade-name">HALVERN</div>
      <div class="abs trade-col" style="left:75px"><small>ENTRY PRICE</small><span>$25.99</span></div>
      <div class="abs trade-col" style="left:160px"><small>EXIT PRICE</small><span>$45.99</span></div>
      <div class="abs trade-col" style="left:234px"><small>CURRENT PROFIT</small><span>$20.99<em class="badge">35%</em></span></div>
    </div>
    <div class="abs sep" style="top:90px"></div>
    <div class="abs trade" style="top:107px">
      <div class="abs trade-mark" style="background:#1e5fa8;border-radius:50%" role="img" aria-label="Velmorix ticker symbol"></div>
      <div class="abs trade-name">VELMORIX</div>
      <div class="abs trade-col" style="left:75px"><small>ENTRY PRICE</small><span>$25.99</span></div>
      <div class="abs trade-col" style="left:160px"><small>EXIT PRICE</small><span>$45.99</span></div>
      <div class="abs trade-col" style="left:234px"><small>CURRENT PROFIT</small><span>$20.99<em class="badge">35%</em></span></div>
    </div>
    <div class="abs sep" style="top:172px"></div>
    <div class="abs trade" style="top:194px">
      <div class="abs trade-mark" style="background:linear-gradient(#d8322b 50%,#2f9e44 50%)" role="img" aria-label="Quillon ticker symbol"></div>
      <div class="abs trade-name">QUILLON</div>
      <div class="abs trade-col" style="left:75px"><small>ENTRY PRICE</small><span>$25.99</span></div>
      <div class="abs trade-col" style="left:160px"><small>EXIT PRICE</small><span>$45.99</span></div>
      <div class="abs trade-col" style="left:234px"><small>CURRENT PROFIT</small><span>$20.99<em class="badge">35%</em></span></div>
    </div>
    <div class="abs sep" style="top:258px"></div>
    <div class="abs trade" style="top:277px">
      <div class="abs trade-mark" style="background:#e6b820" role="img" aria-label="Dorvale ticker symbol"></div>
      <div class="abs trade-name">DORVALE</div>
      <div class="abs trade-col" style="left:75px"><small>ENTRY PRICE</small><span>$25.99</span></div>
      <div class="abs trade-col" style="left:160px"><small>EXIT PRICE</small><span>$45.99</span></div>
      <div class="abs trade-col" style="left:234px"><small>CURRENT PROFIT</small><span>$20.99<em class="badge">35%</em></span></div>
    </div>
  </div>

  <div class="abs copyright">Copyright © 2024 All Rights Reserved</div>
</section>

</body>
</html>
```